Vending machine company website for SnackHarbor

We need a website for our vending machine services company. It will be based on another website that a friend has. My URL is snackharbor.com and the one I'm trying to emulate with my own logo and colors is pantrybloxo.com.

This will be roughly 6 total pages with one being an opt-in/opt-out page for SMS messages, one being a contact form, etc.

I want to use the logo I purchased from this site that I have attached.

The goal is to be clean, professional, intuitive and easy navigation, etc.

The only difference between my site and the reference site should be that we are not offering coffee service.

I will need all of the code for the site, and it should not use any CMS things like Joomla, Wordpress, etc.

Our actual machines are this model minus the green highlights.f

https://www.kelvomat.com/krx-pdl-mq-snack-and-drink-vending-machine-374.html

Target Market(s)

Companies that want to have vending machine services, or to buy or lease vending machines

Industry/Entity Type

Vending machines for snacks and drinks either placed at locations like apartment complexes, waiting rooms for tire centers, office building break rooms, etc. also vending machine repair services, or selling or leasing vending machines to those interested in getting into the business.

Coding

Coded - Design and coding required

Number of Pages Required

5+ page

Font styles to use
Sans Serif

Requirements
Must have
• It will be similar to pantrybloxo.com in terms of pages, categories, etc. but with our logo, colors, etc. and should be clean and professional. It will have the same pages plus one other page for opt-in or opt-out of SMS messages
Nice to have
• Clean graphics and perhaps some AI designs for vending machine repair, just like the one they use on the pantrybloxo.com site. We would like multiple photos on the home page cycling where you see very attractive people shopping for snacks and drinks at the machines with the items blurred, or people sitting around laughing and smiling while enjoying snacks or drinks at a campus break room, or picnic table, or outside with the machine behind them. Please search for KRX-PDL-47M(B2) Snack And Drink Vending Machine at kelvomat
Should not have
• It can not be designed for CRM like WordPress, Joomla, etc. and should be clean new code, that doesn't attract hackers and it shouldn't be too busy.

```html
<!DOCTYPE html>
<html lang="en">
<head>
<meta charset="utf-8">
<title>SnackHarbor — Vending Machine Solutions</title>
<link href="https://fonts.googleapis.com/css2?family=Montserrat:ital,wght@0,400;0,500;0,600;0,700;1,400&display=swap" rel="stylesheet">
<style>
:root{
  --orange:#cf8a2a;
  --orange-btn:#c98420;
  --dark:#1a1a1a;
  --dark-2:#262626;
  --card:#2b2b2b;
  --light:#f3f3f3;
  --ink:#1d1d1d;
  --muted:#6d6d6d;
  --line:#e1e1e1;
}
*{margin:0;padding:0;box-sizing:border-box}
html,body{width:1200px;height:4005px;overflow:hidden}
body{font-family:"Montserrat",sans-serif;color:var(--ink);background:#fff;position:relative}
section,header,footer{position:relative;width:1200px;overflow:hidden}
.abs{position:absolute}
.orange{color:var(--orange)}
.btn{position:absolute;display:flex;align-items:center;justify-content:center;gap:6px;background:var(--orange-btn);color:#fff;font-size:11px;font-weight:700;letter-spacing:.3px;border-radius:3px}
.btn svg{width:10px;height:10px}
.logo{font-weight:600;font-size:24px;display:flex;align-items:center;gap:6px}
.logo .dot{width:10px;height:10px;border-radius:50%;background:var(--orange)}

/* hero */
.hero{height:586px}
.hero-photo{position:absolute;inset:0;background:linear-gradient(100deg,#141414 0%,#262a2c 45%,#3a3c3c 62%,#1e2327 80%,#2a3a44 100%)}
.hero-machines{position:absolute;left:560px;top:148px;width:420px;height:420px;background:linear-gradient(180deg,#3a3f45,#6a5540 55%,#2a2c30);border-radius:4px;opacity:.75}
.nav{position:absolute;left:174px;top:18px;width:852px;height:36px;display:flex;align-items:center;color:#fff}
.nav .logo{color:#fff}
.nav ul{list-style:none;display:flex;gap:26px;position:absolute;left:281px;font-size:9px;font-weight:500;letter-spacing:.2px}
.nav .btn{right:0;top:2px;width:160px;height:34px}
.hero .kicker{left:174px;top:186px;font-size:18px;font-weight:600;color:var(--orange)}
.hero h1{left:174px;top:214px;font-size:34px;line-height:40px;font-weight:700;color:#fff;width:560px}
.hero p{left:174px;top:314px;font-size:11.5px;line-height:20px;color:#e4e4e4;width:390px}
.hero .btn{left:174px;top:376px;width:165px;height:34px}

/* features */
.features{height:263px;background:#fff}
.feature{position:absolute;top:0;width:200px;text-align:center;font-size:10px;line-height:14px;color:#555}
.feature svg{display:block;margin:0 auto 12px;width:38px;height:38px}
.feature.active{background:#f6f6f6;border-radius:2px}

/* products */
.products{height:429px}
.products .left{position:absolute;left:0;top:0;width:600px;height:429px;background:var(--dark)}
.products .right{position:absolute;left:600px;top:0;width:600px;height:429px;background:var(--light)}
.machine{position:absolute;border-radius:6px}
.product .num{font-size:12px;color:var(--orange);margin-bottom:8px}
.product h3{font-size:20px;font-weight:700;margin-bottom:16px}
.product p{font-size:10.5px;line-height:20px}
.product .more{font-size:10px;font-weight:700;color:var(--orange);margin-top:14px}
.products-wrap{height:429px;position:relative;top:-20px}

/* partners */
.partners{height:292px}
.partners h2{left:174px;top:76px;font-size:24px;font-weight:700}
.badge{position:absolute;top:130px;width:161px;height:84px;background:#f7f7f7;display:flex;align-items:center;justify-content:center}
.badge span{display:block;width:92px;height:30px;border-radius:4px;background:#d9d9d9}
.badge.on{border:2px solid var(--orange);background:#fff}

/* services */
.services{height:533px;background:var(--dark);color:#fff}
.services .kicker{left:174px;top:72px;font-size:12px;color:var(--orange)}
.services h2{left:174px;top:90px;font-size:24px;line-height:30px;font-weight:700}
.services .lead{left:558px;top:112px;font-size:10.5px;line-height:20px;color:#cfcfcf;width:470px}
.services .lead b{color:var(--orange);font-size:10px}
.svc{position:absolute;top:174px;width:270px;height:282px;background:var(--card);text-align:center}
.svc .ph{height:154px}
.svc .bar{height:4px;margin:0 12px;background:var(--orange)}
.svc h4{font-size:14.5px;font-weight:700;margin:22px 0 10px}
.svc p{font-size:9.5px;line-height:14px;color:#bdbdbd;padding:0 30px}
.svc .more{font-size:10px;font-weight:700;color:var(--orange);margin-top:12px}

/* testimonials */
.reviews{height:539px;background:#fdfdfd}
.reviews h2{left:174px;top:82px;font-size:24px;font-weight:700}
.reviews .btn{left:887px;top:77px;width:139px;height:33px}
.review{position:absolute;top:138px;width:270px;height:339px;background:#fff;padding:28px 24px}
.review.lift{box-shadow:0 4px 14px rgba(0,0,0,.12);border:1px solid #eee}
.stars{display:flex;gap:5px;margin-bottom:20px}
.stars svg{width:14px;height:14px}
.review h4{font-size:20px;line-height:27px;font-weight:500;margin-bottom:20px}
.review p{font-size:10px;line-height:15.5px;font-style:italic;color:var(--muted)}
.who{display:flex;align-items:center;gap:12px;margin-top:26px;font-size:10px;font-weight:500}
.who span.av{width:34px;height:34px;border-radius:50%;background:linear-gradient(135deg,#8d8d8d,#4a4a4a)}

/* faq */
.faq{height:606px}
.faq h2{left:174px;top:86px;font-size:24px;font-weight:700}
.faq-list{position:absolute;left:174px;top:130px;width:852px}
.faq-item{border-bottom:1px solid var(--line);height:57px;display:flex;align-items:center;justify-content:space-between;font-size:11px;font-weight:500}
.faq-item.open{height:100px;display:block;padding-top:14px}
.faq-item.open .q{display:flex;justify-content:space-between}
.faq-item.open p{font-size:10.5px;line-height:16px;color:var(--muted);margin-top:16px;font-weight:400}
.pm{font-size:18px;font-weight:700}

/* contact */
.contact{height:525px;background:var(--dark);color:#fff}
.contact .machines{left:58px;top:46px;width:440px;height:420px;background:linear-gradient(120deg,#d9d9d9,#9a9a9a 55%,#b8443a 80%,#c6642f);border-radius:6px;opacity:.9}
.contact .kicker{left:566px;top:102px;font-size:12px;color:var(--orange)}
.contact h2{left:566px;top:124px;font-size:24px;font-weight:700}
.field{position:absolute;height:36px;border:1px solid #4a4a4a;background:#222;border-radius:3px;font-size:10px;color:#d6d6d6;padding:0 18px;display:flex;align-items:center}
.contact .btn{left:908px;top:388px;width:118px;height:33px}
.rule{height:9px;background:var(--orange)}

/* footer */
.site-footer{height:223px;background:#fff}
.site-footer .logo{left:174px;top:44px;color:var(--ink);position:absolute;font-size:26px}
.site-footer .about{left:174px;top:94px;width:290px;font-size:9.5px;line-height:16px;color:var(--muted)}
.fcol{position:absolute;top:66px;font-size:10px;color:#444}
.fcol h5{font-size:11.5px;color:var(--orange);font-weight:600;margin-bottom:12px}
.fcol li{list-style:none;margin-bottom:8px;display:flex;gap:8px;align-items:flex-start;line-height:14px}
.fcol svg{width:12px;height:12px;flex:none;margin-top:1px}
.copy{left:0;width:1200px;top:202px;text-align:center;font-size:9px;color:#888}
</style>
</head>
<body>

<header class="hero">
  <div class="hero-photo" role="img" aria-label="Dim modern break room with two snack and drink vending machines"></div>
  <div class="hero-machines" role="img" aria-label="Two stocked snack and drink vending machines"></div>
  <nav class="nav">
    <div class="logo">SnackHarbor<span class="dot"></span></div>
    <ul><li>HOME</li><li>ABOUT US</li><li>OUR MACHINES</li><li>SERVICES</li><li>PARTNERS</li></ul>
    <div class="btn"><svg viewBox="0 0 10 10"><path d="M2 1l2 2-1 1c1 1 2 2 3 3l1-1 2 2-1 1C5 9 1 5 1 2z" fill="#fff"/></svg>CONTACT US</div>
  </nav>
  <div class="abs kicker">REVOLUTIONIZE YOUR BREAK ROOM</div>
  <h1 class="abs">Experience with Our Vending Machine Solutions!</h1>
  <p class="abs">Experience seamless convenience with our cutting-edge vending solutions. Elevate your workplace with our tailored services today.</p>
  <div class="btn"><svg viewBox="0 0 10 10"><path d="M2 1l2 2-1 1c1 1 2 2 3 3l1-1 2 2-1 1C5 9 1 5 1 2z" fill="#fff"/></svg>INQUIRE NOW</div>
</header>

<section class="features">
  <div class="feature" style="left:174px;top:90px">
    <svg viewBox="0 0 38 38"><circle cx="19" cy="19" r="15" fill="none" stroke="#cf8a2a" stroke-width="3" stroke-dasharray="5 3"/><circle cx="19" cy="19" r="6" fill="#cf8a2a"/></svg>
    Fully Automated and Contactless<br>Solutions</div>
  <div class="feature" style="left:391px;top:90px">
    <svg viewBox="0 0 38 38" fill="none" stroke="#cf8a2a" stroke-width="4"><path d="M4 14V4h10M24 4h10v10M34 24v10H24M14 34H4V24"/></svg>
    Bespoke, Flexible and Scalable</div>
  <div class="feature active" style="left:609px;top:75px;height:111px;padding-top:15px">
    <svg viewBox="0 0 38 38"><circle cx="19" cy="19" r="16" fill="#cf8a2a"/><circle cx="19" cy="19" r="11" fill="#fff"/><text x="19" y="23" font-size="10" font-weight="700" text-anchor="middle" fill="#cf8a2a" font-family="Montserrat,sans-serif">24</text></svg>
    24×7 Availability: Relevance with<br>Convenience</div>
  <div class="feature" style="left:826px;top:90px">
    <svg viewBox="0 0 38 38"><circle cx="19" cy="19" r="16" fill="#cf8a2a"/><path d="M12 19l5 5 9-10" fill="none" stroke="#fff" stroke-width="3.5"/></svg>
    Branded, curated, and nutritious<br>range of meals, snacks and<br>beverages</div>
</section>

<section class="products">
  <div class="left"></div><div class="right"></div>
  <div class="machine" style="left:152px;top:0;width:202px;height:418px;background:linear-gradient(90deg,#e8e8e8,#cfd6e6 40%,#9aa9c6 60%,#d46b2e 85%,#c7c7c7)" role="img" aria-label="Compact combo vending machine, white with orange trim"></div>
  <div class="machine" style="left:852px;top:3px;width:276px;height:398px;background:linear-gradient(90deg,#f2f2f2,#d6dde8 40%,#aab6c8 60%,#d4332a 82%,#e6e6e6)" role="img" aria-label="Standard combo vending machine, white with red panel"></div>
  <div class="abs product" style="left:372px;top:77px;width:200px;color:#fff">
    <div class="num">Product 01</div>
    <h3>Compact Combo</h3>
    <p style="color:#cfcfcf">Specifically tailored for locations with limited space or businesses that have fewer staff and customers. Despite its smaller footprint, it provides a convenient range of 30 fully customizable product selections, ensuring that SnackHarbor caters to a diverse array of preferences for both food and beverages.</p>
    <div class="more">KNOW MORE »</div>
  </div>
  <div class="abs product" style="left:625px;top:77px;width:200px">
    <div class="num">Product 02</div>
    <h3>Standard Combo</h3>
    <p style="color:#777">Vending machines that combine snacks and drinks cater to a diverse range of customers. SnackHarbor offers an extensive selection of sweet, salty, healthy, and protein-rich snacks, as well as beverages. With these options, your business can meet everyone's taste preferences.</p>
    <div class="more">KNOW MORE »</div>
  </div>
</section>

<section class="partners">
  <h2 class="abs">Our <span class="orange">Partners</span></h2>
  <div class="badge" style="left:0"><span></span></div>
  <div class="badge" style="left:174px"><span></span></div>
  <div class="badge" style="left:347px"><span></span></div>
  <div class="badge on" style="left:521px"><span></span></div>
  <div class="badge" style="left:693px"><span></span></div>
  <div class="badge" style="left:866px"><span></span></div>
  <div class="badge" style="left:1039px"><span></span></div>
</section>

<section class="services">
  <div class="abs kicker">Our Sevice</div>
  <h2 class="abs">We Offer a Wide Variety<br>of <span class="orange">Vending Sevice</span></h2>
  <p class="abs lead">We provide outstanding vending machine services in the greater San Francisco, South San Francisco, Brisbane, San Mateo, Millbrae, Burlingame, . <b>READ MORE »</b></p>
  <div class="svc" style="left:174px">
    <div class="ph" role="img" aria-label="Colleagues choosing snacks at a vending machine" style="background:linear-gradient(120deg,#d9d4cc,#8c6a4a 50%,#c4b9a8)"></div>
    <div class="bar"></div>
    <h4>Vending Machine Services</h4>
    <p>We offer three types of vending machine services. The most common of them is traditional vending.</p>
    <div class="more">READ MORE »</div>
  </div>
  <div class="svc" style="left:465px">
    <div class="ph" role="img" aria-label="Technician servicing a vending machine" style="background:linear-gradient(120deg,#2c3a55,#a0603a 50%,#3a4a66)"></div>
    <div class="bar"></div>
    <h4>Vending Machine Repairs</h4>
    <p>Technical service for our customers is free, and we are fully responsible for the maintenance of our machines.</p>
    <div class="more">READ MORE »</div>
  </div>
  <div class="svc" style="left:755px">
    <div class="ph" role="img" aria-label="Close view of a dark vending machine front" style="background:linear-gradient(120deg,#1e1e1e,#5a5a5a 50%,#2a2a2a)"></div>
    <div class="bar"></div>
    <h4>Sale or Lease</h4>
    <p>We only deploy our proprietary vending machines that look and work like new to all our clients.</p>
    <div class="more">READ MORE »</div>
  </div>
</section>

<section class="reviews">
  <h2 class="abs">Customers About <span class="orange">SnackHarbor</span></h2>
  <div class="btn"><svg viewBox="0 0 10 10"><path d="M2 1l2 2-1 1c1 1 2 2 3 3l1-1 2 2-1 1C5 9 1 5 1 2z" fill="#fff"/></svg>VIEW ALL</div>

  <div class="review" style="left:174px">
    <div class="stars"><svg viewBox="0 0 10 10"><path d="M5 0l1.5 3.3 3.5.4-2.6 2.4.7 3.5L5 7.8 1.9 9.6l.7-3.5L0 3.7l3.5-.4z" fill="#cf8a2a"/></svg><svg viewBox="0 0 10 10"><path d="M5 0l1.5 3.3 3.5.4-2.6 2.4.7 3.5L5 7.8 1.9 9.6l.7-3.5L0 3.7l3.5-.4z" fill="#cf8a2a"/></svg><svg viewBox="0 0 10 10"><path d="M5 0l1.5 3.3 3.5.4-2.6 2.4.7 3.5L5 7.8 1.9 9.6l.7-3.5L0 3.7l3.5-.4z" fill="#cf8a2a"/></svg><svg viewBox="0 0 10 10"><path d="M5 0l1.5 3.3 3.5.4-2.6 2.4.7 3.5L5 7.8 1.9 9.6l.7-3.5L0 3.7l3.5-.4z" fill="#cf8a2a"/></svg><svg viewBox="0 0 10 10"><path d="M5 0l1.5 3.3 3.5.4-2.6 2.4.7 3.5L5 7.8 1.9 9.6l.7-3.5L0 3.7l3.5-.4z" fill="#c8c8c8"/></svg></div>
    <h4>Sleepe- A Game Changer</h4>
    <p>Lorem ipsum dolor sit amet consectetur. Lacus maecenas lacus placerat id at quis. Tortor quis amet consequat euismod id dignissim id velit. Pretium metus sed pellentesque et. Varius nec venenatis bibendum quam.</p>
    <div class="who"><span class="av"></span>Maren Holt</div>
  </div>
  <div class="review lift" style="left:465px">
    <div class="stars"><svg viewBox="0 0 10 10"><path d="M5 0l1.5 3.3 3.5.4-2.6 2.4.7 3.5L5 7.8 1.9 9.6l.7-3.5L0 3.7l3.5-.4z" fill="#cf8a2a"/></svg><svg viewBox="0 0 10 10"><path d="M5 0l1.5 3.3 3.5.4-2.6 2.4.7 3.5L5 7.8 1.9 9.6l.7-3.5L0 3.7l3.5-.4z" fill="#cf8a2a"/></svg><svg viewBox="0 0 10 10"><path d="M5 0l1.5 3.3 3.5.4-2.6 2.4.7 3.5L5 7.8 1.9 9.6l.7-3.5L0 3.7l3.5-.4z" fill="#cf8a2a"/></svg><svg viewBox="0 0 10 10"><path d="M5 0l1.5 3.3 3.5.4-2.6 2.4.7 3.5L5 7.8 1.9 9.6l.7-3.5L0 3.7l3.5-.4z" fill="#cf8a2a"/></svg><svg viewBox="0 0 10 10"><path d="M5 0l1.5 3.3 3.5.4-2.6 2.4.7 3.5L5 7.8 1.9 9.6l.7-3.5L0 3.7l3.5-.4z" fill="#cf8a2a"/></svg></div>
    <h4>Sleepe- A Game Changer</h4>
    <p>Lorem ipsum dolor sit amet consectetur. Lacus maecenas lacus placerat id at quis. Tortor quis amet consequat euismod id dignissim id velit. Pretium metus sed pellentesque et. Varius nec venenatis bibendum quam.</p>
    <div class="who"><span class="av"></span>Dana Pryce</div>
  </div>
  <div class="review" style="left:755px">
    <div class="stars"><svg viewBox="0 0 10 10"><path d="M5 0l1.5 3.3 3.5.4-2.6 2.4.7 3.5L5 7.8 1.9 9.6l.7-3.5L0 3.7l3.5-.4z" fill="#cf8a2a"/></svg><svg viewBox="0 0 10 10"><path d="M5 0l1.5 3.3 3.5.4-2.6 2.4.7 3.5L5 7.8 1.9 9.6l.7-3.5L0 3.7l3.5-.4z" fill="#cf8a2a"/></svg><svg viewBox="0 0 10 10"><path d="M5 0l1.5 3.3 3.5.4-2.6 2.4.7 3.5L5 7.8 1.9 9.6l.7-3.5L0 3.7l3.5-.4z" fill="#cf8a2a"/></svg><svg viewBox="0 0 10 10"><path d="M5 0l1.5 3.3 3.5.4-2.6 2.4.7 3.5L5 7.8 1.9 9.6l.7-3.5L0 3.7l3.5-.4z" fill="#cf8a2a"/></svg><svg viewBox="0 0 10 10"><path d="M5 0l1.5 3.3 3.5.4-2.6 2.4.7 3.5L5 7.8 1.9 9.6l.7-3.5L0 3.7l3.5-.4z" fill="#c8c8c8"/></svg></div>
    <h4>Sleepe- A Game Changer</h4>
    <p>Lorem ipsum dolor sit amet consectetur. Lacus maecenas lacus placerat id at quis. Tortor quis amet consequat euismod id dignissim id velit. Pretium metus sed pellentesque et. Varius nec venenatis bibendum quam.</p>
    <div class="who"><span class="av"></span>Tessa Lindqvist</div>
  </div>
  <div class="review" style="left:1046px">
    <div class="stars"><svg viewBox="0 0 10 10"><path d="M5 0l1.5 3.3 3.5.4-2.6 2.4.7 3.5L5 7.8 1.9 9.6l.7-3.5L0 3.7l3.5-.4z" fill="#cf8a2a"/></svg><svg viewBox="0 0 10 10"><path d="M5 0l1.5 3.3 3.5.4-2.6 2.4.7 3.5L5 7.8 1.9 9.6l.7-3.5L0 3.7l3.5-.4z" fill="#cf8a2a"/></svg><svg viewBox="0 0 10 10"><path d="M5 0l1.5 3.3 3.5.4-2.6 2.4.7 3.5L5 7.8 1.9 9.6l.7-3.5L0 3.7l3.5-.4z" fill="#cf8a2a"/></svg><svg viewBox="0 0 10 10"><path d="M5 0l1.5 3.3 3.5.4-2.6 2.4.7 3.5L5 7.8 1.9 9.6l.7-3.5L0 3.7l3.5-.4z" fill="#cf8a2a"/></svg><svg viewBox="0 0 10 10"><path d="M5 0l1.5 3.3 3.5.4-2.6 2.4.7 3.5L5 7.8 1.9 9.6l.7-3.5L0 3.7l3.5-.4z" fill="#cf8a2a"/></svg></div>
    <h4>Sleepe- A Game Changer</h4>
    <p>Lorem ipsum dolor sit amet consectetur. Lacus maecenas lacus placerat id at quis. Tortor quis amet consequat euismod id dignissim id velit. Pretium metus sed pellentesque et. Varius nec venenatis bibendum quam.</p>
    <div class="who"><span class="av"></span>Maren Holt</div>
  </div>
</section>

<section class="faq">
  <h2 class="abs">Frequently Aks Question</h2>
  <div class="faq-list">
    <div class="faq-item open">
      <div class="q"><span>How can I get more information about your services?</span><span class="pm">−</span></div>
      <p>For further information about our company or products please contact us by phone or email. If possible, we would like to schedule an in person meeting at your facilities to demonstrate to you how our services can benefit your organization and your collaborators.</p>
    </div>
    <div class="faq-item"><span>Do I need to pay for your vending machine services or for the use of your machines?</span><span class="pm">+</span></div>
    <div class="faq-item"><span>After accepting SnackHarbor services, how long does it take to get the machines?</span><span class="pm">+</span></div>
    <div class="faq-item"><span>Can I select the products in the machines?</span><span class="pm">+</span></div>
    <div class="faq-item"><span>Are your vending machines in good condition?</span><span class="pm">+</span></div>
    <div class="faq-item"><span>Do I need to sign a vending contract?</span><span class="pm">+</span></div>
  </div>
</section>

<section class="contact">
  <div class="abs machines" role="img" aria-label="Two combo vending machines, one with red and one with orange trim"></div>
  <div class="abs kicker">Contact Us</div>
  <h2 class="abs">Need a <span class="orange">vending machine?</span></h2>
  <div class="field" style="left:566px;top:175px;width:222px">First Name*</div>
  <div class="field" style="left:800px;top:175px;width:226px">Last Name*</div>
  <div class="field" style="left:566px;top:227px;width:460px">Email*</div>
  <div class="field" style="left:566px;top:276px;width:460px">Phone Number*</div>
  <div class="field" style="left:566px;top:326px;width:460px">Your Organization and a Brief Description About You*</div>
  <div class="btn"><svg viewBox="0 0 10 10"><path d="M2 1l2 2-1 1c1 1 2 2 3 3l1-1 2 2-1 1C5 9 1 5 1 2z" fill="#fff"/></svg>SEND</div>
</section>
<div class="rule"></div>

<footer class="site-footer">
  <div class="logo">SnackHarbor<span class="dot"></span></div>
  <p class="abs about">SnackHarbor is a locally owned and professionally operated, full service vending business that provides vending machine placement and exceptional services to privately owned businesses, large corporations, and government agencies at no cost.</p>
  <div class="fcol" style="left:524px"><h5>Useful Links</h5><ul><li>About Us</li><li>Our Machines</li><li>Products</li><li>Services</li></ul></div>
  <div class="fcol" style="left:654px"><h5>Legal</h5><ul><li>Terms &amp; Conditions</li><li>Privacy</li><li>Cookies</li></ul></div>
  <div class="fcol" style="left:808px;width:220px"><h5>Contact</h5><ul>
    <li><svg viewBox="0 0 12 12"><path d="M6 0a4 4 0 014 4c0 3-4 8-4 8S2 7 2 4a4 4 0 014-4z" fill="#cf8a2a"/><circle cx="6" cy="4" r="1.5" fill="#fff"/></svg>1180 Harborline Avenue, San Francisco, CA 94107</li>
    <li><svg viewBox="0 0 12 12"><rect x="0" y="2" width="12" height="8" rx="1" fill="#cf8a2a"/><path d="M0 3l6 4 6-4" fill="none" stroke="#fff"/></svg>info@snackharbor.com</li>
    <li><svg viewBox="0 0 12 12"><path d="M2 1l3 3-1.5 1.5c1 1.5 2 2.5 3.5 3.5L8.5 7.5l3 3-1.5 1.5C5 12 0 7 0 2.5z" fill="#cf8a2a"/></svg>(833) 555-0142</li>
  </ul></div>
  <div class="abs copy">Copyright © 2024 SnackHarbor. All Rights Reserved.</div>
</footer>

</body>
</html>
```